Update KORVEN Global's Website

We need to update our current website - www.korvenglobal.example, either with the same template (Joomla 1.5 CMS site using the Plumtrack Meridian) or new one. Please see the first Attached File for additional details of the changes we would like.

A brief summary of changes are:
- Change colors and update the tagline on the logo
- Remove text and add text and pictures
- Remove pages and add a page
and other minor changes

The site is currently hosted at Ta Welbo. You will have access to the FTP file transfer to download and work with the current files.

Please contact me with any questions: derek@korvenglobal.example
Updates

Project Deadline Extended
Reason: Extending to view additional designs. Please indicate if you are proposing a completely new site or redo of the current template. Best, Derek

```html
<!DOCTYPE html>
<html lang="en">
<head>
<meta charset="utf-8">
<title>KORVEN Global — Affordable Housing &amp; Social Investment</title>
<link rel="stylesheet" href="https://fonts.googleapis.com/css2?family=Arimo:wght@400;700&display=swap">
<style>
:root{
  --teal:#16807a;
  --teal-dark:#0f6a65;
  --ink:#1e1e1e;
  --text:#555;
  --muted:#7a7a7a;
  --line:#d8d8d8;
  --panel-head:#7d7d7d;
  --footer:#000;
  --link:#1a73c6;
}
*{box-sizing:border-box;margin:0;padding:0}
html,body{width:1200px;height:1105px;overflow:hidden;background:#fff}
body{font-family:"Arimo",Arial,sans-serif;color:var(--text);position:relative}
.topbar{position:absolute;left:0;top:0;width:1200px;height:13px;background:var(--teal)}
.brand{position:absolute;left:182px;top:36px}
.brand-name{display:flex;align-items:center;gap:8px;font-size:26px;font-weight:700;color:var(--teal);line-height:1}
.brand-mark{width:14px;height:14px;background:var(--teal)}
.brand-tagline{font-size:12px;color:#555;margin-top:5px;padding-left:32px}
.social{position:absolute;left:783px;top:45px;width:28px;height:28px;background:var(--teal)}
.search{position:absolute;left:818px;top:45px;width:200px;height:28px;border:1px solid var(--line);display:flex}
.search-field{flex:1;font-size:8.5px;color:#888;padding:9px 8px}
.search-btn{width:29px;background:#e9e9e9;display:flex;align-items:center;justify-content:center}
.nav-rule{position:absolute;top:116px;height:1px;background:#888}
.nav{position:absolute;left:209px;top:103px;height:25px;width:820px}
.nav a{font-size:12px;color:#666;text-decoration:none;position:absolute;white-space:nowrap;top:7px}
.nav a.active{background:var(--teal);color:#fff;font-weight:700;padding:6px 10px;top:0}
.hero{position:absolute;left:0;top:154px;width:1200px;height:428px;background:linear-gradient(90deg,#cfcac4 0%,#e8e5e1 25%,#f1efec 45%,#bcd4e4 62%,#a9c4d6 80%,#c9bfae 100%)}
.hero-card{position:absolute;left:618px;top:43px;width:426px;height:342px;background:rgba(255,255,255,.9);padding:22px 38px}
.hero-card h1{font-size:24px;color:var(--ink);font-weight:700;margin-bottom:12px}
.hero-card p{font-size:10px;line-height:15.2px;text-align:justify;color:#333;margin-bottom:15px}
.btn{display:inline-block;margin-top:8px;background:var(--teal);color:#fff;font-size:13px;padding:11px 17px;border-bottom:2px solid var(--teal-dark)}
.arrow{position:absolute;top:196px;width:37px;height:37px;background:rgba(22,128,122,.6);display:flex;align-items:center;justify-content:center;z-index:2}
.dots{position:absolute;top:399px;left:576px;display:flex;gap:6px}
.dots span{width:12px;height:12px;border-radius:50%;border:2px solid #fff}
.dots span.on{background:var(--teal);border-color:var(--teal)}
.welcome{position:absolute;left:182px;top:634px;width:441px}
.welcome h2{font-size:14px;color:var(--ink);font-weight:700;margin-bottom:16px}
.welcome ul{list-style:none;margin-bottom:15px}
.welcome li{font-size:11.6px;color:var(--ink);line-height:17px;padding-left:15px;position:relative}
.welcome li::before{content:"";position:absolute;left:2px;top:7px;width:4px;height:4px;border-radius:50%;background:var(--ink)}
.welcome p{font-size:10.2px;line-height:16.6px;text-align:justify;margin-bottom:16.6px}
.panel{position:absolute;border:1px solid var(--line)}
.panel-head{background:var(--panel-head);color:#fff;font-weight:700;font-size:11.5px;text-align:center;height:27px;line-height:27px;margin:-1px -1px 0}
.invest{left:669px;top:628px;width:167px;height:213px;overflow:hidden}
.invest h3{font-size:11.5px;color:var(--ink);text-align:center;line-height:17px;margin-top:11px}
.invest-photo{position:absolute;right:0;bottom:0;width:135px;height:128px;background:linear-gradient(160deg,#f4f4ef 0%,#d7e3c9 45%,#e6cfb6 100%)}
.partner{left:669px;top:858px;width:167px;height:81px;display:flex;align-items:center;justify-content:center}
.partner-badge{width:110px;height:44px;background:linear-gradient(90deg,#3aa0c8,#56b56a)}
.offices{left:852px;top:628px;width:167px;height:311px}
.office{padding:11px 12px;font-size:10.2px;line-height:16.6px;color:var(--muted)}
.office+.office{border-top:1px solid var(--line)}
.office strong{display:block;font-size:11.6px;color:var(--ink);margin-bottom:1px}
.office a{color:var(--link);text-decoration:none;font-size:9.8px}
.footer{position:absolute;left:0;top:1000px;width:1200px;height:105px;background:var(--footer);color:#fff;text-align:center}
.footer-links{font-size:10.2px;margin-top:19px}
.footer-links span{margin:0 9px}
.copyright{font-size:10.2px;margin-top:18px}
</style>
</head>
<body>
<div class="topbar"></div>

<div class="brand">
  <div class="brand-name"><span class="brand-mark"></span>KORVEN Global</div>
  <div class="brand-tagline">Affordable Housing &amp; Social Investment</div>
</div>

<div class="social" aria-label="Social profile"></div>
<div class="search">
  <div class="search-field">to search, type and hit enter</div>
  <div class="search-btn">
    <svg width="16" height="16" viewBox="0 0 16 16"><circle cx="9.5" cy="6.5" r="4.5" fill="none" stroke="#111" stroke-width="2"/><line x1="6.3" y1="9.7" x2="1.5" y2="14.5" stroke="#111" stroke-width="2.4"/></svg>
  </div>
</div>

<div class="nav-rule" style="left:0;width:169px"></div>
<div class="nav-rule" style="left:1032px;width:168px"></div>
<nav class="nav">
  <a class="active" style="left:0">Home</a>
  <a style="left:100px">Community Development</a>
  <a style="left:286px">Affordable Housing</a>
  <a style="left:442px">Alternative Energy</a>
  <a style="left:592px">KORVEN Team</a>
  <a style="left:714px">Contact Us</a>
</nav>

<section class="hero" role="img" aria-label="Bright modern apartment interior with a white kitchen counter, bar stool and a window view over the city and sea">
  <article class="hero-card">
    <h1>Vistamar Lofts</h1>
    <p>Lorem Ipsum is simply dummy text of the printing and typesetting industry. Lorem Ipsum has been the industry's standard dummy text ever since the 1500s, when an unknown printer took a galley of type and scrambled it to make a type specimen book. It has survived not only five centuries, but also the leap into electronic typesetting, remaining essentially unchanged. It was popularised in the 1960s with the release of Letraset sheets containing Lorem Ipsum passages, and more recently with desktop publishing software like Aldus PageMaker including versions of Lorem Ipsum.</p>
    <p>Lorem Ipsum is simply dummy text of the printing and typesetting industry. Lorem Ipsum has been the industry's standard dummy text ever since the 1500s, when an unknown printer took a galley of type and scrambled it to make a type specimen book.</p>
    <span class="btn">Read the Full Story</span>
  </article>
  <div class="arrow" style="left:183px"><svg width="10" height="14" viewBox="0 0 10 14"><path d="M7 1 1 7l6 6" fill="none" stroke="#fff" stroke-width="1.6"/></svg></div>
  <div class="arrow" style="left:981px"><svg width="10" height="14" viewBox="0 0 10 14"><path d="M3 1l6 6-6 6" fill="none" stroke="#fff" stroke-width="1.6"/></svg></div>
  <div class="dots"><span class="on"></span><span></span><span></span></div>
</section>

<section class="welcome">
  <h2>WELCOME TO KORVEN GLOBAL.</h2>
  <ul>
    <li>Community Development.</li>
    <li>Affordable Green Housing.</li>
    <li>Sustainable Alternative Energy.</li>
  </ul>
  <p>KORVEN is a socially responsible corporation working in the areas of affordable housing and alternative energy.</p>
  <p>We at KORVEN think environmental and social accountability are as fundamental as making a profit. In fact, they go hand in hand. All our projects—from the development of affordable green housing to an island eco-lodge and residences—specialize in superior investment and ownership opportunities and employ the latest in sustainable and green technologies.</p>
  <p>Our vision is to create and support eco-friendly, sustainable property developments in Panama that maximize profit for our investors and strengthen communities for our neighbors.</p>
  <p>KORVEN Global: the next generation of sustainable real estate development in Panama.</p>
</section>

<aside class="panel invest">
  <div class="panel-head">SOCIAL INVESTMENTS</div>
  <h3>Contact KORVEN for Social<br>Investment Opportunities</h3>
  <div class="invest-photo" role="img" aria-label="Photo: cupped hands holding a small green globe"></div>
</aside>

<aside class="panel partner">
  <div class="partner-badge" aria-label="Partner project badge"></div>
</aside>

<aside class="panel offices">
  <div class="panel-head">OFFICES</div>
  <div class="office">
    <strong>KORVEN Panama, S.A.</strong>
    Panama Office<br>Via Brisamar, Plaza Coralina<br>#24<br>Panama City, Panama<br>Ofc: 507-555-0142<br>Fax: 507-555-0187<br>
    <a>contact@korvenglobal.example</a>
  </div>
  <div class="office">
    <strong>KORVEN Global, LLC</strong>
    U.S. Office<br>418 Alder Crest Way, #305<br>Marlow, WA 98990<br>Ofc: 206-555-0119<br>Fax: 206-555-0173
  </div>
</aside>

<footer class="footer">
  <div class="footer-links">Home<span>|</span>Community Development<span>|</span>Affordable Housing<span>|</span>Eco Tourism<span>|</span>Alternative Energy<span>|</span>KORVEN Team<span>|</span>Contact Us<span>|</span>Privacy Policy<span>|</span>Sitemap</div>
  <div class="copyright">© Copyright 2009-2014 KORVEN Global, LLC. All Rights Reserved.</div>
</footer>
</body>
</html>
```